Local Restaurant Needs a One Page Breakfast Menu

I own a restaurant and we are going to be starting a new breakfast service. I want a one page menu that is clean, bright, and tongue in cheek. We will only have a limited menu, so there should be plenty of space to work with. I will not want actual food pictures, but more of a cartoon style representations of food. I'd like a modern cartoon style mixed with our current 1950s theme.

Name of Restaurant: Marlow's
Location: 2493 W. Larch. Pellton, MO 58214 - Phone: 555-014-3047 (including location is not a requirement)

Breakfast Hours: 6:30 am - 10:30 am

The two colors selected below are not required, but they are the two colors that are featured inside the dining room of the restaurant.

Industry/Entity Type

Restaurant

Colors
8667ad
acd036

Requirements
Must have
• Menu must only be one page (either standard letter or oversized - either would be ok).

Menu items:

Stuffed Omellete. Stuffing choices: cheese, peppers, jalapenos, onions, tomatoes, salsa, sour cream, green onions, sausage, bacon, ham

Marlow's Blintz (thin, stuffed, pancakes): Stuffing choices: chocolate chips, Q&Zs, Talbot's Nibbles, strawberries, blueberries, raspberries, bananas, sour cream

Homemade Coffee Cake

Cinnamon Rolls

Beverages - Coffee, Soda, Milk

Prices not set (use placeholders).

```html
<!DOCTYPE html>
<html lang="en">
<head>
<meta charset="utf-8">
<title>Marlow's Breakfast Menu</title>
<link rel="stylesheet" href="https://fonts.googleapis.com/css2?family=Archivo+Black&family=Oswald:wght@400;600&family=Roboto+Condensed:wght@300&family=Yellowtail&display=swap">
<style>
  :root {
    --lime: #acd036;
    --purple: #8667ad;
    --ink: #1c1c1c;
    --paper: #ffffff;
    --rule: #9a9a9a;
  }
  * { margin: 0; padding: 0; box-sizing: border-box; }
  html, body { width: 927px; height: 1200px; overflow: hidden; background: var(--paper); }
  .menu { position: relative; width: 927px; height: 1200px; color: var(--ink); font-family: "Oswald", sans-serif; }

  .brand {
    position: absolute; left: 270px; top: 110px; width: 387px;
    text-align: center;
  }
  .brand-name {
    font-family: "Archivo Black", sans-serif; font-size: 46px; line-height: 1.1;
    color: var(--purple); letter-spacing: 2px;
  }
  .brand-contact {
    font-family: "Oswald", sans-serif; font-weight: 400; font-size: 14px;
    color: var(--ink); margin-top: 22px; line-height: 1.5; letter-spacing: 0.5px;
  }

  .art { position: absolute; border-radius: 10px; }
  .art-sugar { left: 124px; top: 113px; width: 106px; height: 145px; background: linear-gradient(var(--lime), #9cc02c); }
  .art-coffee { left: 711px; top: 106px; width: 121px; height: 136px; background: linear-gradient(#ffffff, #e8e4ef); border: 2px solid var(--ink); }
  .art-chef { left: 204px; top: 998px; width: 121px; height: 128px; background: linear-gradient(var(--purple), #755a9c); border-radius: 40px 40px 12px 12px; }
  .art-milk { left: 408px; top: 965px; width: 91px; height: 169px; background: linear-gradient(var(--lime), var(--purple)); }
  .art-shakers { left: 665px; top: 1028px; width: 76px; height: 91px; background: linear-gradient(90deg, var(--lime) 50%, var(--purple) 50%); }

  .rule { position: absolute; left: 0; width: 927px; border-top: 2px dotted var(--rule); }
  .rule-label {
    position: absolute; left: 50%; top: -17px; transform: translateX(-50%);
    background: var(--paper); padding: 0 14px;
    font-family: "Yellowtail", cursive; font-size: 24px; line-height: 32px; color: var(--ink);
  }

  .hours { position: absolute; top: 408px; width: 100%; text-align: center; font-family: "Oswald", sans-serif; font-weight: 600; font-size: 17px; line-height: 23px; letter-spacing: 0.5px; }

  .item { position: absolute; width: 100%; text-align: center; }
  .item-title { font-family: "Archivo Black", sans-serif; font-weight: 400; font-size: 24px; letter-spacing: 5px; line-height: 1; }
  .item-price { font-family: "Yellowtail", cursive; font-size: 27px; letter-spacing: 0; margin-left: 6px; font-weight: 400; }
  .item-note { font-family: "Yellowtail", cursive; font-size: 20px; letter-spacing: 0; margin-right: 6px; font-weight: 400; }
  .item-fillings { font-family: "Oswald", sans-serif; font-size: 13px; line-height: 20px; margin-top: 8px; letter-spacing: 0.2px; }
  .item-omelette { top: 520px; }
  .item-blintzes { top: 610px; }
  .item-cake { top: 702px; }
  .item-rolls { top: 755px; }

  .drinks { position: absolute; top: 870px; width: 100%; text-align: center; font-family: "Roboto Condensed", sans-serif; font-weight: 300; font-size: 42px; letter-spacing: 1px; }
</style>
</head>
<body>
<main class="menu">
  <header class="brand">
    <h1 class="brand-name">MARLOW'S<br>FOR BREAKFAST</h1>
    <p class="brand-contact">2493 W. LARCH. PELLTON, MO 58214<br>P: 555-014-3047</p>
  </header>

  <div class="art art-sugar" role="img" aria-label="Cartoon lime sugar canister"></div>
  <div class="art art-coffee" role="img" aria-label="Cartoon coffee percolator with purple lid"></div>

  <div class="rule" style="top:390px"></div>
  <p class="hours">BREAKFAST HOURS<br>6:30 AM - 10:30 AM</p>
  <div class="rule" style="top:484px"><span class="rule-label">Food</span></div>

  <section class="item item-omelette">
    <h2 class="item-title">STUFFED OMLETTE<span class="item-price">$7.95</span></h2>
    <p class="item-fillings">STUFF IT: CHEESE, PEPPERS, JALAPENOS, ONIONS, TOMATOES,<br>SALSA, SOUR CREAM, GREEN ONIONS, SAUSAGE, BACON, HAM</p>
  </section>

  <section class="item item-blintzes">
    <h2 class="item-title">MARLOW'S BLINTZES<span class="item-price">$7.95</span></h2>
    <p class="item-fillings">STUFF IT: BANANAS, Q&amp;ZS, TALBOT'S NIBBLES, SOUR CREAM<br>STRAWBERRIES, BLUEBERRIES, RASPBERRIES, CHOC. Q&amp;ZS</p>
  </section>

  <section class="item item-cake">
    <h2 class="item-title"><span class="item-note">Homemade*</span>COFFEE CAKE<span class="item-price">$4.95</span></h2>
  </section>

  <section class="item item-rolls">
    <h2 class="item-title">CINNAMON ROLLS<span class="item-price">$5.95</span></h2>
  </section>

  <div class="rule" style="top:835px"><span class="rule-label">Bevarages</span></div>
  <p class="drinks">COFFE, SODA, MILK</p>
  <div class="rule" style="top:945px"></div>

  <div class="art art-chef" role="img" aria-label="Cartoon purple chef's hat"></div>
  <div class="art art-milk" role="img" aria-label="Cartoon milk carton in lime and purple"></div>
  <div class="art art-shakers" role="img" aria-label="Cartoon salt and pepper shakers"></div>
</main>
</body>
</html>
```